Medical Software Informational Flyer and Website Design

Our company, Copper Vale Systems, is launching a new product, the Copper Vale Clinic Workflow Hub. It is a software suite that will increase the productivity and volume of a LASIK practice.

We want this flyer to be a companion to our big reveal presentation at OLV and PEMWG; it's primary purpose is to inform potential clients on the many ways this software will help their practice. It is also obviously a promotional material. Because it is a companion to our presentation, we feel that it is acceptable for the flyer to contain much more text than would normally be reasonable in a flyer; it will go into more detail about the 12 major selling points of our software than our presentation time will allow. Having said that, however, we still want there to be "breathing room" for the design and the viewer's eyes.

We have uploaded our logo, both in full color and in white with no background (often used for watermarks, but certainly not restricted for that use alone). Our logo should be accompanied by either "Copper Vale Systems" or "Copper Vale" using the Trajan Pro font (unoriginal, we know, but it's what we've chosen). We have included a color palette that compliments our logo, but designs are not limited to that palette (for example, we have found a pink (#cc1448) that compliments the palette and that we have used in the presentation).

We have also uploaded a PSD that includes icons that could compliment 9 of the 12 major selling points for the Copper Vale Clinic Workflow Hub software (the category titles are subject to change). The icons are not necessarily set in stone. For consistency with our presentation, the Protection, Integration, and Review icons should be used, but any of the remaining six (in particular, the Personalized icon) can be changed to whatever you think might be more suitable. The PSD also has some preliminary text for a few of the 12 selling points (we are refining the text now and will get the final content to designers very soon). Also note that the font is simply a placeholder; use whatever font you think would best compliment your design. Finally, keep in mind that the PSD does NOT reflect a design we are looking for; in fact, we hate this "design" and hesitate to call it a design. It was simply a way to arrange the elements to easily distribute them to designers.

We want an 8 1/2in x 11in 8-page flyer that is professional, simple, and has a clear message: this product will revolutionize your practice! We of course also need a website design that compliments the flyer design once the flyer design is finalized and chosen.

We will be monitoring this project closely-- please ask any questions you have!
Updates

Target Market(s)

Physicians, technicians, and marketing personnel in the LASIK industry.

Industry/Entity Type

Software

Number of Pages Required

4 page

Font styles to use
Serif
Sans Serif

```html
<!DOCTYPE html>
<html lang="en">
<head>
<meta charset="utf-8">
<title>Copper Vale Systems — Flyer</title>
<link rel="stylesheet" href="https://fonts.googleapis.com/css2?family=Didact+Gothic&display=swap">
<style>
  :root {
    --stage: #5a2f17;
    --navy: #062a35;
    --green: #15876a;
    --yellow: #f2cb12;
    --ink-light: #f4f1e6;
    --ink-dark: #1f2a22;
    --label: #ffffff;
    --back-panel: #3e2113;
  }
  * { box-sizing: border-box; margin: 0; padding: 0; }
  html, body { width: 1200px; height: 750px; overflow: hidden; }
  body {
    position: relative;
    background: var(--stage);
    font-family: "Didact Gothic", "Helvetica Neue", Arial, sans-serif;
  }
  .side-label {
    position: absolute; top: 27px;
    font-size: 10px; color: var(--label); letter-spacing: 0.02em;
  }
  .side-label--front { left: 103px; }
  .side-label--back { left: 646px; }

  .page { position: absolute; top: 51px; height: 648px; }
  .page--front { left: 95px; width: 501px; background: var(--navy); overflow: hidden; }
  .page--back { left: 645px; width: 502px; background: var(--back-panel); }

  .masthead { position: absolute; left: 0; top: 0; width: 501px; height: 161px; }
  .brand-dot {
    position: absolute; left: 36px; top: 62px;
    width: 86px; height: 86px; border-radius: 50%; background: var(--green);
  }
  .brand-name {
    position: absolute; left: 142px; top: 88px;
    font-family: "Didact Gothic", "Helvetica Neue", Arial, sans-serif;
    font-weight: 400; font-size: 30px; line-height: 1;
    color: var(--ink-light); white-space: nowrap;
  }

  .block { position: absolute; overflow: hidden; font-size: 8.4px; line-height: 9.9px; }
  .block p { position: relative; z-index: 1; }
  .block p + p { margin-top: 10px; }
  .block--green { background: var(--green); color: var(--ink-light); }
  .block--yellow { background: var(--yellow); color: var(--ink-dark); }
  .block--navy { color: var(--ink-light); }

  .intro { left: 0; top: 161px; width: 251px; height: 184px; padding: 28px 22px 0 28px; }
  .contact { left: 251px; top: 161px; width: 250px; height: 184px; padding: 32px 22px 0 26px; }
  .integration { left: 0; top: 345px; width: 501px; height: 160px; padding: 44px 52px 0 39px; }
  .protection-a { left: 0; top: 505px; width: 255px; height: 143px; padding: 29px 52px 0 30px; }
  .protection-b { left: 255px; top: 505px; width: 246px; height: 143px; padding: 24px 50px 0 26px; }

  .faint-icon { position: absolute; z-index: 0; }
  .faint-icon--arrows { left: 182px; top: 138px; width: 66px; height: 44px; background: var(--ink-light); border-radius: 4px; opacity: 0.1; }
  .faint-icon--puzzle { left: 0; top: 116px; width: 86px; height: 44px; background: #2e5260; opacity: 0.5; }
  .faint-icon--stars { left: 150px; top: 100px; width: 90px; height: 90px; border-radius: 50%; background: #fff3b0; opacity: 0.35; }
  .faint-icon--umbrella { left: 196px; top: 98px; width: 50px; height: 44px; border-radius: 25px 25px 0 0; background: var(--ink-light); opacity: 0.12; }
</style>
</head>
<body>
  <span class="side-label side-label--front">FRONT</span>
  <span class="side-label side-label--back">BACK</span>

  <main class="page page--front">
    <header class="masthead">
      <span class="brand-dot" aria-hidden="true"></span>
      <h1 class="brand-name">Copper Vale Systems</h1>
    </header>

    <section class="block block--green intro">
      <div class="faint-icon faint-icon--arrows" role="img" aria-label="Faint connection arrows icon"></div>
      <p>It’s time for a revolution in an industry that depends on effective marketing, tracking marketing campaign effectiveness, and converting interest into procedures. Finally comes the solution: the Copper Vale Clinic Workflow Hub which includes connectivity between your marketing records and your patient records.</p>
      <p>Two databases, one for patients and one for prospective patients, with a single program connecting them. It’s simple, it’s HIPAA-compliant, and it’s only the beginning.</p>
    </section>

    <section class="block block--yellow contact">
      <p>Contact with prospective and current patients is key in a market of elective procedures. Communication must be efficient, standardized, but also personalized. The Copper Vale Clinic Workflow Hub does it all by incorporating the patient and contact database information in your communications. The Suite offers an array of customizable, personalized emails, texts, and even printouts for appointment reminders, surgery preparation information, and referral programs - all with a few clicks.</p>
    </section>

    <section class="block block--navy integration">
      <div class="faint-icon faint-icon--puzzle" role="img" aria-label="Faint puzzle pieces integration icon"></div>
      <p>In the digital age our industry still requires patients to fill out forms with pen and paper which in turn have to be entered into a database by hand.</p>
      <p>Technicians must take digital information from [device], print it out into physical paper, then enter the data back into digital format. We say, “No more.” With the Copper Vale Clinic Workflow Hub your practice will enjoy full digital integration of all key equipment, including the laser, the Wavefront, and the HIPAA-compliant databases that connect them.</p>
    </section>

    <section class="block block--yellow protection-a">
      <div class="faint-icon faint-icon--stars" role="img" aria-label="Faint review stars icon"></div>
      <p>With your key devices linked together in an integrated system, the Copper Vale Clinic Workflow Hub offers significant protection for you and your practice. In addition to streamlining operations, not having to enter data multiple times means you are protected from human errors that can lead to lawsuits.</p>
    </section>

    <section class="block block--green protection-b">
      <div class="faint-icon faint-icon--umbrella" role="img" aria-label="Faint protection umbrella icon"></div>
      <p>With your key devices linked together in an integrated system, the Copper Vale Clinic Workflow Hub offers significant protection for you and your practice. In addition to streamlining operations, not having to enter data multiple times means you are protected from human errors that can lead to lawsuits.</p>
    </section>
  </main>

  <aside class="page page--back" aria-label="Back page"></aside>
</body>
</html>
```